Point of Sale Systems Web Design Project

I need a complete redesign of my existing website. I sell point of sale systems and need to seamlessly combine the features, products and services of several companies I represent. The current site is at www.tillgroveplaza.com. The new site will be rebranded as www.TradeZoral.com. I will be adding products from www.quaylinkpro.com, www.pinrowly.com, www.dakswivo.com as well as other similar products and services such as http://kelbafund.com/homepage_USA.html

The new tag line will be:
Electronic Payment Systems Made ZORAL!
Updates

I have made a change to the website name. The new name will be TradeZoral.com. I look forward to seeing the designs. Please see http://www.zoral.com.au/index.html for the inspiration behind the new name. I am also going to increase the budget for this project. Thank you

Target Market(s)

These are products and services for business owners. We provide Credit Card Processing Equipment and Processing Services to Retail, Restaurant, Home-based, and Internet businesses.

Industry/Entity Type

Electronic

Requirements
Must have
• Visitors need to be able to view video demos and download PDF documents. Site should be easy to update with new products or services.
Nice to have
• Designs I like: http://www.thebrivelworks.com, http://www.plantyourbalconies.com, http://www.qortalvistagroup.com/

```html
<!DOCTYPE html>
<html lang="en">
<head>
<meta charset="utf-8">
<title>TradeZoral.com – Electronic Payment Solutions</title>
<link rel="stylesheet" href="https://fonts.googleapis.com/css2?family=Didact+Gothic&family=Nunito+Sans:wght@700;800&display=swap">
<style>
:root{
  --sky:#cfe6f7;
  --panel:#ffffff;
  --blue:#1aa0e2;
  --blue-dark:#0a7fc8;
  --banner-a:#0b8fe0;
  --banner-b:#32b4f2;
  --hero-panel:#cde6f6;
  --button:#cfe8f8;
  --grey-head:#555b60;
  --text:#333;
  --text-soft:#555;
  --red:#c0200f;
  --red-link:#d01010;
  --line:#d8dde2;
  --field-border:#dfe5ea;
}
*{box-sizing:border-box;margin:0;padding:0}
html,body{width:1112px;height:1200px;overflow:hidden;background:var(--sky)}
body{font-family:"Didact Gothic",sans-serif;color:var(--text)}
.stage{position:relative;width:1073px;height:1158px;transform:scale(1.0363);transform-origin:0 0}
.page{position:absolute;left:41px;top:0;width:991px;height:1142px;background:var(--panel);box-shadow:0 2px 8px rgba(0,0,0,.18)}
.abs{position:absolute}
.head-font{font-family:"Nunito Sans",sans-serif;font-weight:800}

/* header */
.top-strip{left:0;top:0;width:991px;height:133px;background:var(--sky)}
.banner{left:9px;top:12px;width:974px;height:92px;border:3px solid #fff;border-radius:4px;
  background:linear-gradient(90deg,var(--banner-a) 0%,#4fc3f7 28%,var(--banner-a) 45%,var(--banner-b) 100%);
  box-shadow:0 2px 4px rgba(0,0,0,.2)}
.brand{left:24px;top:26px;font-family:"Nunito Sans",sans-serif;font-weight:800;font-size:32px;color:#fff;display:flex;align-items:center;gap:10px}
.brand-dot{width:14px;height:14px;background:#fff;border-radius:50%}
.phone{left:627px;top:26px;font-size:27px;color:#fff;letter-spacing:.5px}
.social{left:831px;top:29px;display:flex;gap:7px}
.social span{width:22px;height:22px;border-radius:4px;background:rgba(255,255,255,.85)}
.social svg{margin-left:2px}
.nav{left:358px;top:110px;display:flex;gap:0}
.nav a{font-family:"Nunito Sans",sans-serif;font-weight:800;font-size:15px;color:#4a4f55;text-decoration:none}

/* hero */
.hero-panel{left:0;top:145px;width:327px;height:320px;background:var(--hero-panel);border-radius:0 6px 6px 0}
.hero-photo{left:0;top:150px;width:320px;height:314px;background:linear-gradient(135deg,#f3e6d6 0%,#e9ecef 55%,#c9ccd0 100%)}
.tagline{left:358px;top:164px;font-size:27px;color:var(--grey-head);letter-spacing:.3px}
.hero-title{left:358px;top:228px;font-size:28px;color:var(--blue);letter-spacing:.2px}
.hero-copy{left:358px;top:265px;width:610px;font-size:14.2px;line-height:16px;color:#222}
.btn{top:413px;height:38px;background:var(--button);border:1px solid #bcd9ee;box-shadow:1px 2px 2px rgba(0,0,0,.12);
  font-family:"Nunito Sans",sans-serif;font-weight:800;font-size:13px;line-height:14px;color:#3a4a58;padding:4px 0 0 20px}
.btn-terminal{left:361px;width:148px}
.btn-process{left:533px;width:148px}
.btn-arrow{position:absolute;right:6px;top:3px}
.pdf{left:910px;top:406px;text-align:center;font-size:9px;color:#444;width:50px}
.divider{left:40px;top:468px;width:800px;height:2px;background:linear-gradient(90deg,transparent,#d4d8dc 20%,#d4d8dc 80%,transparent)}

/* features */
.feature{top:505px;width:290px}
.feature h3{font-size:16px;line-height:20px;color:#222;margin-bottom:6px;letter-spacing:.2px}
.feature p{font-size:12.5px;line-height:19.5px;color:var(--text-soft)}
.col-rule{top:510px;width:0;height:245px;border-left:1px dashed #c8cdd2}
.product{height:72px;border-radius:3px}
.maker{font-family:"Didact Gothic",sans-serif;font-size:19px;color:#777;margin-top:6px}
.video-btn{top:738px;width:95px;height:24px;background:var(--button);border:1px solid #c4def0;font-size:11px;color:#fff;
  font-family:"Nunito Sans",sans-serif;font-weight:700;padding:4px 0 0 8px}
.video-btn svg{position:absolute;right:5px;top:4px}

/* lower area */
.lower{left:0;top:805px;width:991px;height:288px;background:linear-gradient(180deg,#ffffff 0%,#dcedf9 100%)}
.lower-rule{left:20px;top:803px;width:620px;height:2px;background:linear-gradient(90deg,transparent,#d0d5da 15%,#d0d5da 85%,transparent)}
.notch{left:140px;top:788px;width:40px;height:20px;border-radius:20px 20px 0 0;border:2px solid #e2e6ea;border-bottom:none;background:#fff}
.quote-title{left:185px;top:842px;font-size:17px;color:var(--red);font-family:"Nunito Sans",sans-serif;font-weight:800}
.label{left:35px;font-size:12px;color:#333}
.field{left:183px;width:193px;height:20px;background:#fff;border:1px solid var(--field-border)}
.select{left:183px;top:937px;width:192px;height:19px;background:#f5f6f7;border:1px solid #d5dade;font-size:11px;color:#444;padding:2px 5px}
.select i{position:absolute;right:2px;top:2px;width:14px;height:13px;background:#ccd2d8}
.textarea{left:183px;top:963px;width:193px;height:70px;background:#fff;border:1px solid var(--field-border)}
.quote-cta{left:183px;top:1042px;font-size:16px;color:var(--red)}
.v-rule{left:430px;top:830px;width:0;height:245px;border-left:1px solid #e3e8ec}
.news-img{left:486px;width:124px;height:97px;border:1px solid #c9cdd1;padding:4px;background:#fff}
.news-img div{width:100%;height:100%}
.news-title{left:647px;font-size:15.5px;color:var(--blue);font-family:"Nunito Sans",sans-serif;font-weight:800}
.news-date{left:647px;font-size:11.5px;color:#222;font-family:"Nunito Sans",sans-serif;font-weight:700}
.news-copy{left:647px;width:305px;font-size:11.8px;line-height:15.5px;color:#333;letter-spacing:.3px}
.news-more{left:647px;font-size:11.5px;color:var(--red-link);font-family:"Nunito Sans",sans-serif;font-weight:800}

/* footer */
.footer{left:0;top:1093px;width:991px;height:49px;background:#d2e8f7;border-top:2px solid #fff}
.partner{left:186px;top:1102px;width:104px;height:30px;border-radius:4px;background:#b9d3c2}
.copy-mark{left:316px;top:1101px;font-size:16px;color:#333}
.legal{left:341px;top:1103px;font-size:12.3px;line-height:15px;color:#333}
</style>
</head>
<body>
<div class="stage">
  <div class="page">
    <!-- header -->
    <div class="abs top-strip"></div>
    <div class="abs banner"></div>
    <div class="abs brand"><span class="brand-dot"></span>TradeZoral.com</div>
    <div class="abs phone">888-555-0142</div>
    <div class="abs social">
      <span></span><span></span><span></span><span></span>
      <svg width="24" height="20" viewBox="0 0 24 20" aria-label="Email"><rect x="1" y="2" width="22" height="16" rx="1" fill="none" stroke="#fff" stroke-width="2"/><path d="M1 3 L12 12 L23 3" fill="none" stroke="#fff" stroke-width="2"/></svg>
    </div>
    <nav class="abs nav">
      <a href="#" style="margin-left:0">Home</a>
      <a href="#" style="margin-left:49px">About</a>
      <a href="#" style="margin-left:48px">Solutions</a>
      <a href="#" style="margin-left:47px">Services</a>
      <a href="#" style="margin-left:47px">Equipment</a>
      <a href="#" style="margin-left:47px">Contact</a>
    </nav>

    <!-- hero -->
    <div class="abs hero-panel"></div>
    <div class="abs hero-photo" role="img" aria-label="Photo of a smiling woman holding a credit card in front of a laptop"></div>
    <h1 class="abs tagline head-font">Electronic Payment Solutions Made ZORAL!</h1>
    <h2 class="abs hero-title head-font">POS Technology, Systems And Solutions</h2>
    <p class="abs hero-copy">No storefront. No problem. Do you have a PC or Laptop connected to the internet?<br>
      Start processing credit card transactions from any computer with an internet connection.<br>
      Manually process mail and telephone credit&nbsp; card transactions or swipe card via a USB card swiper. Just like a traditional terminal, but with the added flexubility of giving you access from any interne connection&nbsp; in the world.<br>
      There's no hardware to purchase&nbsp; or soft to download. It's flexible, low-cost and trouble free.</p>
    <a class="abs btn btn-terminal">Virtual<br>Terminal</a>
    <a class="abs btn btn-process">Process<br>Payments
      <svg class="btn-arrow" width="32" height="32" viewBox="0 0 32 32" aria-hidden="true"><circle cx="16" cy="16" r="14" fill="#fff" stroke="#9cc9e8" stroke-width="2"/><path d="M13 10 L19 16 L13 22" fill="none" stroke="#1a8fd6" stroke-width="3"/></svg>
    </a>
    <div class="abs pdf">
      <svg width="26" height="28" viewBox="0 0 26 28" aria-hidden="true"><path d="M3 1 H18 L24 7 V27 H3 Z" fill="#fff" stroke="#999"/><rect x="6" y="11" width="15" height="8" fill="#d62b1f"/></svg>
      <div>PDF&nbsp; Details</div>
    </div>
    <div class="abs divider"></div>

    <!-- features -->
    <section class="abs feature" style="left:36px">
      <h3 class="head-font">Pinrowly Salon</h3>
      <p>software does everything you've come to expect rom a salon software POS system - and so much more. The simple touch screen and finger-friendly salon software design will have you moving at salon speed in no time.</p>
      <div class="product" style="margin:18px 0 0 52px;width:150px;height:80px;background:linear-gradient(135deg,#4a4d52,#c9ccd0)" role="img" aria-label="Salon POS touch screen terminal with printer and card reader"></div>
    </section>
    <div class="abs col-rule" style="left:337px"></div>
    <section class="abs feature" style="left:358px">
      <h3 class="head-font">Complet and Affordable POS Solutions for Retai and Hospitality Merchants!</h3>
      <p>Choose from a variety of accessories that are designed specifically with the retail and restaurante environment!</p>
      <div class="product" style="margin:20px 0 0 62px;width:152px;height:82px;background:linear-gradient(135deg,#1b6fd0,#0a3f8c)" role="img" aria-label="POS monitor, receipt printer and PIN pad on blue tiles"></div>
    </section>
    <div class="abs col-rule" style="left:664px"></div>
    <section class="abs feature" style="left:685px">
      <h3 class="head-font">Accepting Credit Cards Has Never Been Easier.</h3>
      <p>Dakswivo is a free app and free credit card reader that transforms your smartphone into a mobile point-of-sale terminal.</p>
      <div class="maker">Dakswivo</div>
      <div class="product" style="margin:8px 0 0 52px;width:155px;height:78px;background:linear-gradient(135deg,#3a3d40,#dfe6e0)" role="img" aria-label="Smartphones with a card reader attached"></div>
    </section>
    <a class="abs video-btn" style="left:38px">View video<svg width="16" height="16" viewBox="0 0 16 16" aria-hidden="true"><circle cx="8" cy="8" r="7" fill="#fff"/><path d="M6 4 L10 8 L6 12" fill="none" stroke="#d01010" stroke-width="2"/></svg></a>
    <a class="abs video-btn" style="left:360px">View video<svg width="16" height="16" viewBox="0 0 16 16" aria-hidden="true"><circle cx="8" cy="8" r="7" fill="#fff"/><path d="M6 4 L10 8 L6 12" fill="none" stroke="#d01010" stroke-width="2"/></svg></a>
    <a class="abs video-btn" style="left:687px">View video<svg width="16" height="16" viewBox="0 0 16 16" aria-hidden="true"><circle cx="8" cy="8" r="7" fill="#fff"/><path d="M6 4 L10 8 L6 12" fill="none" stroke="#d01010" stroke-width="2"/></svg></a>

    <!-- quote form and news -->
    <div class="abs lower"></div>
    <div class="abs lower-rule"></div>
    <div class="abs notch"></div>
    <div class="abs quote-title">Get a FREE quote!</div>
    <div class="abs label" style="top:877px">Full name:</div>
    <div class="abs label" style="top:900px">Email:</div>
    <div class="abs label" style="top:923px">Phone:</div>
    <div class="abs label" style="top:942px">Type of inquires:</div>
    <div class="abs label" style="top:1005px">Additional information:</div>
    <div class="abs field" style="top:867px"></div>
    <div class="abs field" style="top:890px"></div>
    <div class="abs field" style="top:913px"></div>
    <div class="abs select">Select<i></i></div>
    <div class="abs textarea"></div>
    <div class="abs quote-cta">Get Quote Now!</div>
    <div class="abs v-rule"></div>

    <div class="abs news-img" style="top:830px"><div style="background:linear-gradient(135deg,#2e7d3a,#2358b8,#d9dde2)" role="img" aria-label="Fanned stack of gift and credit cards"></div></div>
    <div class="abs news-title" style="top:828px">Gift Cards</div>
    <div class="abs news-date" style="top:852px">1.06.2011</div>
    <p class="abs news-copy" style="top:873px">Suspendisse nibh pede, ultrices vitae, ltrices nec... Nam et augue. Sed a elit. Ut vel massa. Suspendisse nibh pede ultrices vitae, ltrices nec..</p>
    <div class="abs news-more" style="top:926px">Learn more ...</div>

    <div class="abs news-img" style="top:968px"><div style="background:linear-gradient(135deg,#8a6a4a,#c9b59a,#e6e0d6)" role="img" aria-label="Stack of payment cards on a wooden table"></div></div>
    <div class="abs news-title" style="top:966px">Merchant Cash Advance</div>
    <div class="abs news-date" style="top:984px">3.06.2011</div>
    <p class="abs news-copy" style="top:1003px">Suspendisse nibh pede, ultrices vitae, ltrices nec... Nam et augue. Sed a elit. Ut vel massa. Suspendisse nibh pede ultrices vitae, ltrices nec..</p>
    <div class="abs news-more" style="top:1054px">Learn more ...</div>

    <!-- footer -->
    <div class="abs footer"></div>
    <div class="abs partner" aria-label="Certified partner badge"></div>
    <div class="abs copy-mark">©</div>
    <p class="abs legal">Crestline Acceptance Group Registered Sales Agent for Veltora Payments Inc.<br>Member Bank: Brindlecove Bank N.A., Marlow Creek, CA - Member.FDIC</p>
  </div>
</div>
</body>
</html>
```